Upscale Children's Boutique Needs a PSD Web Design

We need a PSD web design for an online children's boutique called 'Pimbrel'. We specialize in special occasion wear for infants. Our apparel products are typically selected for christening & baptisms, birthdays, holidays and weddings. We would like to see designs that compliment our existing logo and business card. The final design should communicate a sense of luxury, but also be fun and oriented towards children.
Our current website is www.pimbrel.com. Note: Not all products are loaded.
Changes to the color scheme, fonts, background and graphics are welcome. And while we like the layout of my current VendaLoft theme (Quillan), we do expect that SMALL modifications will be needed to make it ours. For example, we would like the cart to be placed more visibly. I have a designer that can code the changes you come up with so feel free to suggest what you feel is best.
We look forward to your designs. Good luck!
Websites we like:
https://www.shopwenzabloom.com/ (The layout of this site is nice to me)
http://www.orlaycupboard.com/
http://www.brightvaleharvest.com/
Updates
This contest is for PSD design only. No Vendaloft development or coding is required.
Target Market(s)
Our typical customer is female age 20-45 shopping for her own child or for a gift.
Industry/Entity Type
Boutique
Requirements
Must have
- PSD Design
- These 5 items listed below are things we’d like:
- (1) General styling (color scheme, fonts, background, graphics, etc.) & layout
- • ONLY the logo colors are set … feel free to add colors that compliment it
- • Prefer narrow (or single line) footer
- • We think the main banner/image is too large
- (2) Create main banner/image (current template uses 970px wide)
- (3) AT LEAST Three (3) Marketing banners (current template uses 433 x 225):
- • Our Hottest Products
- • Our Newest Arrivals
- • Newsletter sign-up
- (4) Border to enclose admin links (My account, Gift Certificates, Create an Account)
- (5) New badges / icon / images
- • Shopping Cart --> Bag or cart image should stand out; try to place above search bar (you’ll have to lower the search bar to do this)
- • Sale Badge --> anything goes. Could be a badge or a sash. Might also be nice to have these for the bestsellers as well.
- • Star Icons for product reviews (optional) --> Keep the stars just have them be more stylized
Nice to have
- We like pages that have a background and think one might look good on our site if not too busy.
Should not have
- We do not like extremely dark backgrounds for web pages.

```html
<!DOCTYPE html>
<html lang="en">
<head>
<meta charset="utf-8">
<title>Pimbrel Childrenswear</title>
<link rel="stylesheet" href="https://fonts.googleapis.com/css2?family=Nunito+Sans:ital,wght@0,400;0,600;0,700;0,800;1,600&family=Tinos&display=swap">
<style>
:root{
  --bg:#fbf8f6;
  --ink:#3a3a3a;
  --muted:#777;
  --teal:#5cbfbf;
  --cyan:#5fd1df;
  --peach:#fca87c;
  --amber:#fdbb5e;
  --pink:#f0425a;
  --line:#c9c9c9;
  --dark:#3b3b3b;
  --darker:#2b2b2b;
  --star:#f2c31b;
}
*{box-sizing:border-box;margin:0;padding:0}
html,body{width:777px;height:1200px;overflow:hidden}
body{background:var(--bg);font-family:"Nunito Sans",sans-serif;color:var(--ink);position:relative}
.abs{position:absolute}
.topbar{left:72px;top:0;width:632px;height:40px;border:1px dashed var(--line);border-top:none}
.admin-links{left:84px;top:13px;display:flex;gap:16px;font-size:9px;color:var(--muted)}
.admin-links span::before{content:"";display:inline-block;width:7px;height:7px;border-radius:2px;background:var(--teal);margin-right:5px;vertical-align:-1px}
.search{left:464px;top:8px;width:132px;height:24px;border:1px solid #ddd;background:#fff;font-size:9px;color:#aaa;padding:6px 7px}
.search svg{position:absolute;right:6px;top:6px}
.cart-btn{left:604px;top:9px;width:28px;height:22px;background:var(--teal)}
.cart-total{left:640px;top:14px;font-size:9px;color:var(--muted)}
.brand{left:0;width:777px;top:60px;text-align:center;font-size:40px;font-weight:600;color:var(--teal);letter-spacing:1px}
.brand i{display:inline-block;width:26px;height:26px;border-radius:50%;background:var(--teal);margin-right:10px;vertical-align:4px}
.mainnav{left:72px;top:134px;width:632px;height:38px;border:1px dashed var(--line);display:flex;font-size:11.5px;color:#555}
.mainnav span{position:absolute;top:12px}
.hero{left:71px;top:178px;width:418px;height:266px;background:linear-gradient(110deg,#d9d6d4,#b9b1ad 55%,#e8e4e1)}
.hero h1{position:absolute;left:21px;top:56px;font-size:16px;font-weight:400;color:#222}
.hero p{position:absolute;left:22px;top:81px;width:240px;font-size:9.5px;line-height:14px;color:#333}
.btn{display:inline-block;background:var(--teal);color:#fff;font-size:10px;text-align:center}
.hero .btn{position:absolute;left:20px;top:118px;width:74px;height:21px;line-height:21px}
.side{left:506px;width:200px;height:126px}
.side .photo{position:absolute;right:0;top:0;width:105px;height:126px}
.side h2{position:absolute;left:13px;top:26px;font-family:Tinos,serif;font-weight:400;font-size:13px}
.side h3{position:absolute;left:13px;top:41px;font-weight:400;font-size:13px;color:#666}
.side .btn{position:absolute;left:14px;top:66px;width:74px;height:20px;line-height:20px}
.promo{top:478px;width:199px;height:114px;border:3px solid;outline:1px solid;outline-offset:2px;text-align:center;color:#fff}
.promo .tab{position:absolute;left:50%;top:-25px;margin-left:-22px;width:44px;height:22px;border-radius:22px 22px 0 0}
.promo .tab b{position:absolute;left:16px;top:7px;width:12px;height:12px;border:2px solid #fff;border-radius:50%}
.promo h2{margin-top:17px;font-size:16px;font-weight:700}
.promo p{margin-top:8px;font-size:9.5px;font-style:italic;font-weight:600;color:#222}
.promo .wbtn{display:inline-block;margin-top:10px;background:#fff;color:#333;font-size:10px;width:64px;height:25px;line-height:25px}
.featured{left:71px;top:608px;font-family:Tinos,serif;font-size:17px;color:#222}
.featured-rule{left:268px;top:618px;width:436px;height:1px;background:#e2e2e2}
.product{top:645px;width:150px;text-align:center}
.product .shot{height:141px;border:1px solid #e3e3e3;background:#f7f7f7;position:relative}
.product .shot div{position:absolute;left:35px;top:30px;width:80px;height:80px;border-radius:40%;background:radial-gradient(#fff,#e9e9e9)}
.product.active .shot{border-color:var(--teal)}
.price{margin-top:12px;font-family:Tinos,serif;font-size:18px;color:#222}
.pname{margin-top:6px;font-size:9.5px;line-height:13px;color:#555;height:26px}
.stars{font-size:9px;letter-spacing:1px;color:var(--star);margin-top:-12px;height:12px}
.stars s{text-decoration:none;color:#ddd}
.choose{display:block;margin:10px auto 0;width:103px;height:30px;line-height:30px;background:#2d2d2d;color:#fff;font-family:Tinos,serif;font-size:11px}
.product.active .choose{background:var(--teal)}
.ship{left:71px;top:924px;width:636px;height:58px;background:#fff;border:1px solid #e4e4e4;border-bottom:3px solid #cfdcdc}
.ship .free{position:absolute;left:20px;top:8px;width:46px;height:20px;background:var(--teal);color:#fff;font-weight:800;font-size:13px;text-align:center;line-height:20px}
.ship h2{position:absolute;left:129px;top:6px;font-size:28px;font-weight:400;color:#444;line-height:30px}
.ship h2 b{color:var(--teal);font-weight:800}
.ship .on{position:absolute;left:129px;top:37px;font-size:10.5px;color:#555}
.ship .sep{position:absolute;left:378px;top:10px;width:1px;height:36px;background:#777}
.ship .offer{position:absolute;left:413px;top:9px;font-size:9.5px;line-height:13px;color:#666}
.ship .offer em{font-style:normal;color:var(--teal)}
.ship .badge{position:absolute;left:545px;top:-6px;width:68px;height:52px;background:var(--cyan);border:2px solid #fff;border-radius:6px 6px 50% 50%/6px 6px 20% 20%;color:#fff;font-weight:800;font-size:13px;text-align:center;line-height:14px;padding-top:10px;box-shadow:0 1px 3px rgba(0,0,0,.2)}
.footer{left:0;top:1001px;width:777px;height:167px;background:var(--dark);color:#fff}
.footer h4{position:absolute;top:25px;font-size:11.5px;font-weight:600}
.footer ul{position:absolute;top:51px;list-style:none;font-size:8.5px;line-height:20px}
.footer .intro{position:absolute;left:71px;top:47px;width:130px;font-size:8px;line-height:10px}
.footer .field{position:absolute;left:71px;width:121px;height:18px;background:#fff;color:#777;font-size:8.5px;padding:3px 8px}
.footer .sub{position:absolute;left:71px;top:126px;width:64px;height:18px;line-height:18px;background:var(--teal);font-size:9px;text-align:center}
.contact{position:absolute;left:600px;top:55px;font-size:10.5px;line-height:15px}
.social{position:absolute;left:600px;top:88px;display:flex;gap:6px}
.social i{width:15px;height:15px;border-radius:50%}
.legal{left:0;top:1168px;width:777px;height:32px;background:var(--darker);color:#fff;font-size:8.5px}
.legal span{position:absolute;top:11px}
</style>
</head>
<body>

<div class="abs topbar"></div>
<div class="abs admin-links"><span>My Account</span><span>Gift Certificates</span><span>Create An Account</span><span>View Cart</span></div>
<div class="abs search">Search
  <svg width="11" height="11" viewBox="0 0 11 11"><circle cx="4.5" cy="4.5" r="3.5" fill="none" stroke="#999" stroke-width="1.2"/><line x1="7" y1="7" x2="10" y2="10" stroke="#999" stroke-width="1.2"/></svg>
</div>
<div class="abs cart-btn">
  <svg width="28" height="22" viewBox="0 0 28 22"><path d="M8 6h2l2 8h7l2-6H11" fill="none" stroke="#fff" stroke-width="1.4"/><circle cx="13" cy="16.5" r="1.2" fill="#fff"/><circle cx="18" cy="16.5" r="1.2" fill="#fff"/></svg>
</div>
<div class="abs cart-total">0 item - $ 0.00</div>

<div class="abs brand"><i></i>Pimbrel</div>

<nav class="abs mainnav">
  <span style="left:39px">NEW BABY</span>
  <span style="left:148px">CHRISTENING &amp; BAPTISM</span>
  <span style="left:334px">BIRTHDAY</span>
  <span style="left:441px">HOLIDAY</span>
  <span style="left:541px">WEDDING</span>
</nav>

<section class="abs hero" role="img" aria-label="Photo of a smiling baby lying on a soft blanket">
  <h1>Special Occasion Bibs &amp; Pieces</h1>
  <p>Lorem ipsum dolor sit amet, consectetur adipisc ing elit, sed do eiusmod tempor incididunt ut.</p>
  <span class="btn">Shop Now</span>
</section>

<section class="abs side" style="top:178px;background:#a9e1e8">
  <div class="photo" role="img" aria-label="Photo of a laughing baby in a striped outfit" style="background:linear-gradient(90deg,#a9e1e8,#d9c7b8 60%,#bfe4ea)"></div>
  <h2 style="color:#3fb7c7">OUR BIRTHDAY</h2>
  <h3>Products</h3>
  <span class="btn" style="background:var(--teal)">Shop Now</span>
</section>
<section class="abs side" style="top:318px;background:#f7c6d0">
  <div class="photo" role="img" aria-label="Photo of a smiling baby crawling" style="background:linear-gradient(90deg,#f7c6d0,#ead7ca 60%,#f5cfd7)"></div>
  <h2 style="color:#e8344f">NEW BABY</h2>
  <h3>Products</h3>
  <span class="btn" style="background:var(--pink)">Shop Now</span>
</section>

<section class="abs promo" style="left:71px;background:var(--peach);border-color:#fff;outline-color:var(--peach)">
  <div class="tab" style="background:var(--peach)"><b></b></div>
  <h2>Our Hottest Products</h2>
  <p>Get Upto 30 % off</p>
  <span class="wbtn">Shop Now</span>
</section>
<section class="abs promo" style="left:290px;background:var(--cyan);border-color:#fff;outline-color:var(--cyan)">
  <div class="tab" style="background:var(--cyan)"><b></b></div>
  <h2>Our Newest Arrivals</h2>
  <p>Get Upto 30 % off</p>
  <span class="wbtn">Shop Now</span>
</section>
<section class="abs promo" style="left:507px;background:var(--amber);border-color:#fff;outline-color:var(--amber)">
  <div class="tab" style="background:var(--amber)"><b></b></div>
  <h2>Summer Collections</h2>
  <p>Get Upto 30 % off</p>
  <span class="wbtn">Shop Now</span>
</section>

<h2 class="abs featured">FEATURED PRODUCTS</h2>
<div class="abs featured-rule"></div>

<article class="abs product" style="left:71px">
  <div class="shot"><div role="img" aria-label="White organza christening booties"></div></div>
  <div class="price">$14.00</div>
  <div class="pname">Organza Trim Christening<br>Bootie White</div>
  <span class="choose">CHOOSE OPTION</span>
</article>
<article class="abs product active" style="left:232px">
  <div class="shot"><div role="img" aria-label="White embroidered cotton bib with lace trim"></div></div>
  <div class="price">$11.00</div>
  <div class="pname">Embroidered Cotton Bib<br>With Lace Trim White</div>
  <span class="choose">CHOOSE OPTION</span>
</article>
<article class="abs product" style="left:394px">
  <div class="shot"><div role="img" aria-label="White satin baby booties"></div></div>
  <div class="price">$43.00</div>
  <div class="pname">Satin Bootie</div>
  <div class="stars">★★★★★</div>
  <span class="choose">CHOOSE OPTION</span>
</article>
<article class="abs product" style="left:555px">
  <div class="shot"><div role="img" aria-label="White satin vest and shorts set with hat"></div></div>
  <div class="price">$12.00</div>
  <div class="pname">Satin Vest Shorts</div>
  <div class="stars">★★★<s>★★</s></div>
  <span class="choose">CHOOSE OPTION</span>
</article>

<section class="abs ship">
  <div class="free">FREE</div>
  <svg class="abs" style="left:20px;top:28px" width="80" height="24" viewBox="0 0 80 24">
    <rect x="0" y="2" width="46" height="10" fill="#2d2d2d"/>
    <path d="M48 4h12l8 8v6H48z" fill="#2d2d2d"/>
    <rect x="0" y="12" width="68" height="4" fill="#2d2d2d"/>
    <circle cx="14" cy="18" r="5" fill="#2d2d2d" stroke="#fff" stroke-width="2"/>
    <circle cx="58" cy="18" r="5" fill="#2d2d2d" stroke="#fff" stroke-width="2"/>
  </svg>
  <h2><b>FREE</b> SHIPPING</h2>
  <div class="on">On all <b>ONLINE</b> orders of $50 or more</div>
  <div class="sep"></div>
  <div class="offer">Limited time offer<br>for members only.<br><em>GET FREE SHIPPING</em></div>
  <div class="badge">Shop<br>Now!</div>
</section>

<footer class="abs footer">
  <h4 style="left:71px">NEWSLETTER SUBSCRIBE</h4>
  <p class="intro">Lorem ipsum dolor sit amet, consectetur adipiscing elit.</p>
  <div class="field" style="top:77px">First Name</div>
  <div class="field" style="top:102px">Email</div>
  <div class="sub">SUBSCRIBE</div>

  <h4 style="left:294px">FURTHER INFO</h4>
  <ul style="left:294px"><li>Contact Us</li><li>Blog</li><li>Shipping &amp; Returns</li><li>RSS Syndication</li><li>Sitemap</li></ul>

  <h4 style="left:458px">CATEGORY</h4>
  <ul style="left:458px"><li>New Baby</li><li>Christening &amp; Baptism</li><li>Birhday</li><li>Holiday</li><li>Wedding</li></ul>

  <h4 style="left:601px">CONNECT WITH US</h4>
  <div class="contact">(555) 204 - 7781<br>info@pimbrel.com</div>
  <div class="social"><i style="background:#3b5ea8"></i><i style="background:#3aa9e0"></i><i style="background:#4fbf8f"></i><i style="background:#dd4b39"></i></div>
</footer>

<div class="abs legal">
  <span style="left:71px">© 2015 www.pimbrel.com.All Rights Reserved.</span>
  <span style="left:548px">Terms and Conditions &nbsp; | &nbsp; Privacy Policy</span>
</div>

</body>
</html>
```